Vostra new design for business cards we want to change our existing design. Logo must remain the same

Hello we are the company VoSTra and offer various services regarding transportation and disposal. In addition to our main acquisition of van rental, we also offer disposal and express transportation, so we need new business card designs for our business. Our elders have their time and do not like it anymore. We want to change our existing design. Logo must remain the same as well as the color blue, whether dark or light Does not play a big role in the best medium blue. Logo must be present on the front side. As well as telephone, email, web and location. Big enough but not too big. Back can be redesigned Logo as well as name VoSTra must be present. Important is the text: Van rental Disposal and clearing express transportation. Without bail in red should be noted somewhere. it should be modern but not too playful. rather serious but no beating company Thank you very much

Target Market(s)

Private customers as well as companies we want to change our existing design. Logo must remain the same as well as the color blue, whether dark or light Does not play a big role in the best medium blue. Logo must be present on the front side. As well as telephone, email, web and location. Big enough but not too big. Back can be redesigned Logo as well as name VoSTra must be present. Important is the text: Van rental Disposal and clearing express transportation. Without bail in red should be noted somewhere. it should be modern but not too playful. rather serious but no beating company Thank you very much

Industry/Entity Type

Car Rental

Contact Information for Business Card

we want to change our existing design. Logo must remain the same as well as the color blue, whether dark or light Does not play a big role in the best medium blue.
Logo must be present on the front side.
As well as telephone, email, web and location. Big enough but not too big.
Back can be redesigned Logo as well as name VoSTra must be present.
Important is the text:
Van rental
Disposal and clearing
Express transportation.
Without bail in red should be noted somewhere.
it should be modern but not too playful. rather serious but no beating company
Thank you very much

Font styles to use
Sans Serif

Colors
33a6d7
ec1f27
0692cd
3277b5

Requirements
Must have
• logo and name VoSTra as described in the above text must have it. we want to change our existing design. Logo must remain the same as well as the color blue, whether dark or light Does not play a big role in the best medium blue. Logo must be present on the front side. As well as telephone, email, web and location. Big enough but not too big. Back can be redesigned Logo as well as name VoSTra must be present. Important is the text: Van rental Disposal and clearing express transportation. Without bail in red should be noted somewhere. it should be modern but not too playful. rather serious but no beating company Thank you very much
Nice to have
• see description we want to change our existing design. Logo must remain the same as well as the color blue, whether dark or light Does not play a big role in the best medium blue. Logo must be present on the front side. As well as telephone, email, web and location. Big enough but not too big. Back can be redesigned Logo as well as name VoSTra must be present. Important is the text: Van rental Disposal and clearing express transportation. Without bail in red should be noted somewhere. it should be modern but not too playful. rather serious but no beating company Thank you very much
Should not have
• Blue White and little red we want to change our existing design. Logo must remain the same as well as the color blue, whether dark or light Does not play a big role in the best medium blue. Logo must be present on the front side. As well as telephone, email, web and location. Big enough but not too big. Back can be redesigned Logo as well as name VoSTra must be present. Important is the text: Van rental Disposal and clearing express transportation. Without bail in red should be noted somewhere. it should be modern but not too playful. rather serious but no beating company Thank you very much

```html
<!DOCTYPE html>
<html lang="en">
<head>
<meta charset="utf-8">
<title>VoSTra GmbH – Business Cards</title>
<link rel="stylesheet" href="https://fonts.googleapis.com/css2?family=Roboto:wght@400;500;700&family=Roboto+Condensed:wght@500;700&display=swap">
<style>
  :root {
    --navy: #0b0b6f;
    --steel: #7f9bb7;
    --steel-soft: #dfe6ee;
    --ink: #4a4a4a;
    --rule: #c9c9c9;
    --paper: #f4f4f4;
    --stage: #e7e4df;
    --alert: #e8141c;
  }
  * { margin: 0; padding: 0; box-sizing: border-box; }
  html, body { width: 1200px; height: 960px; overflow: hidden; }
  body {
    position: relative;
    background: var(--stage);
    font-family: "Roboto", Arial, sans-serif;
    color: var(--ink);
  }
  .card {
    position: absolute;
    width: 600px;
    height: 343px;
    background: var(--paper);
    overflow: hidden;
  }
  .card--front { left: 314px; top: 113px; }
  .card--back  { left: 311px; top: 472px; }

  /* front */
  .edge { position: absolute; top: 0; bottom: 0; width: 16px; }
  .edge--left  { left: 0;  background: var(--navy); }
  .edge--right { right: 0; background: var(--steel); }

  .brand {
    position: absolute;
    left: 72px;
    top: 144px;
    display: flex;
    align-items: center;
    gap: 12px;
  }
  .brand__mark { width: 26px; height: 26px; background: var(--navy); }
  .brand__name {
    font-weight: 700;
    font-size: 35px;
    letter-spacing: 1px;
    color: var(--navy);
    line-height: 1;
  }

  .divider {
    position: absolute;
    left: 349px;
    top: 84px;
    width: 1px;
    height: 158px;
    background: var(--rule);
  }
  .contact { position: absolute; left: 381px; top: 82px; }
  .contact__name {
    font-family: "Roboto Condensed", Arial, sans-serif;
    font-weight: 700;
    font-size: 22px;
    color: var(--navy);
    line-height: 26px;
  }
  .contact__role {
    font-family: "Roboto Condensed", Arial, sans-serif;
    font-weight: 500;
    font-size: 16px;
    color: var(--steel);
    line-height: 20px;
  }
  .contact__address {
    margin-top: 9px;
    font-size: 15px;
    line-height: 19px;
    font-style: normal;
  }
  .contact__list { list-style: none; margin-top: 9px; }
  .contact__list li {
    display: flex;
    align-items: center;
    gap: 9px;
    font-size: 15px;
    line-height: 19px;
  }
  .contact__list svg { width: 13px; height: 13px; fill: var(--navy); flex: none; }

  /* back */
  .back-accent {
    position: absolute;
    left: 330px;
    top: 60px;
    width: 220px;
    height: 220px;
    background: var(--steel-soft);
  }
  .back-brand {
    position: absolute;
    left: 36px;
    top: 174px;
    font-weight: 700;
    font-size: 46px;
    letter-spacing: 1px;
    color: var(--navy);
    line-height: 1;
  }
  .services {
    position: absolute;
    left: 36px;
    top: 233px;
    list-style: none;
    font-size: 15px;
    line-height: 19px;
  }
  .services li::before {
    content: "";
    display: inline-block;
    width: 4px; height: 4px;
    border-radius: 50%;
    background: var(--navy);
    margin: 0 10px 3px 2px;
  }
  .notice {
    position: absolute;
    left: 35px;
    top: 299px;
    font-size: 15px;
    color: var(--alert);
  }
</style>
</head>
<body>

  <section class="card card--front" aria-label="Business card front">
    <div class="edge edge--left"></div>
    <div class="edge edge--right"></div>

    <div class="brand">
      <span class="brand__mark"></span>
      <span class="brand__name">VOSTRA</span>
    </div>

    <div class="divider"></div>

    <div class="contact">
      <p class="contact__name">LUKAS MEIER</p>
      <p class="contact__role">CEO/FOUNDER</p>
      <address class="contact__address">Lindenweg 14<br>8500 Frauenfeld</address>
      <ul class="contact__list">
        <li>
          <svg viewBox="0 0 24 24" aria-hidden="true"><path d="M6.6 10.8a15.1 15.1 0 0 0 6.6 6.6l2.2-2.2c.3-.3.7-.4 1-.2 1.1.4 2.3.6 3.6.6.6 0 1 .4 1 1V20c0 .6-.4 1-1 1A17 17 0 0 1 3 4c0-.6.4-1 1-1h3.5c.6 0 1 .4 1 1 0 1.3.2 2.5.6 3.6.1.3 0 .7-.2 1z"/></svg>
          +41 76 430 22 18
        </li>
        <li>
          <svg viewBox="0 0 24 24" aria-hidden="true"><path d="M2 5h20v14H2zm2 2v.5l8 5 8-5V7zm0 2.8V17h16V9.8l-8 5z"/></svg>
          info@vostra.ch
        </li>
        <li>
          <svg viewBox="0 0 24 24" aria-hidden="true"><path d="M12 2a10 10 0 1 0 0 20 10 10 0 0 0 0-20zm-1 17.9A8 8 0 0 1 4.2 10.2L9 15v1a2 2 0 0 0 2 2zm6.9-2.5A2 2 0 0 0 16 16h-1v-3a1 1 0 0 0-1-1H8v-2h2a1 1 0 0 0 1-1V7h2a2 2 0 0 0 2-2v-.4a8 8 0 0 1 2.9 12.8z"/></svg>
          www.VoSTra.ch
        </li>
      </ul>
    </div>
  </section>

  <section class="card card--back" aria-label="Business card back">
    <div class="back-accent"></div>
    <p class="back-brand">VOSTRA</p>
    <ul class="services">
      <li>Van rental</li>
      <li>Disposal &amp; clearing</li>
      <li>Express transportation</li>
    </ul>
    <p class="notice">Without bail</p>
  </section>

</body>
</html>
```